KTV Catapult

I need a graphic package design for our new bodybuilding sports supplement. The artwork should be clean and useable for many formats. examples or great usage are www.brawnvelta.example, www.sinewcore.example and http://www.pellarynutrition.example/ as examples. I am adding our logo for your reference. The name Catapult is because it will help make "Big Guns" as a catch phrase, the product line will have other supplements such as creatine and protein powders and the artwork should be useable on all products. You can see our website for ideas at www.kestovalelabs.example
Updates

Hi everyone, There are some nice entries coming in. I do wonder if some of you are reading the brief as a few labels don't even highlight the product, KTV is the company, Catapult is the Product. Thanks Dex

Industry/Entity Type

Supplement

```html
<!DOCTYPE html>
<html lang="en">
<head>
<meta charset="utf-8">
<title>KTV Catapult – Chewable Label Set</title>
<link rel="stylesheet" href="https://fonts.googleapis.com/css2?family=Russo+One&family=Audiowide&family=Montserrat:wght@700&family=Share+Tech+Mono&display=swap">
<style>
  :root {
    --page: #5e5e5e;
    --label-black: #0b0b0c;
    --label-edge: #1c1c1f;
    --white: #ffffff;
    --band-light: #f2f2f2;
    --band-mid: #9a9a9a;
    --band-dark: #5c5c5c;
    --band-text: #ffffff;
    --rule: #d8d8d8;
  }
  html, body {
    margin: 0;
    padding: 0;
    width: 1200px;
    height: 756px;
    overflow: hidden;
  }
  body {
    background: var(--page);
    position: relative;
    font-family: "Audiowide", sans-serif;
  }
  .label {
    position: absolute;
    top: 236px;
    width: 254px;
    height: 434px;
    background: var(--label-black);
    border-radius: 6px;
    box-shadow: inset 0 0 0 1px var(--label-edge);
    overflow: hidden;
  }
  .label--blue   { left: 183px; --accent: #7fc8ff; --accent-deep: #1b5fae; --bullet: #ff3d9a; --name: #ffffff; --tag-new: #ff2d8c; --tag-chew: #ff8a1c; }
  .label--orange { left: 471px; --accent: #ffb36b; --accent-deep: #a4460c; --bullet: #3fb4ff; --name: #ffffff; --tag-new: #ff2d2d; --tag-chew: #ffffff; }
  .label--red    { left: 760px; --accent: #d9d9d9; --accent-deep: #6a6a6a; --bullet: #e01a1a; --name: #d0141b; --tag-new: #25d6d0; --tag-chew: #ffffff; }

  .label__burst {
    position: absolute;
    left: 0;
    top: 78px;
    width: 254px;
    height: 158px;
    background:
      radial-gradient(ellipse 60% 55% at 52% 62%, var(--accent) 0%, var(--accent-deep) 38%, transparent 72%),
      linear-gradient(200deg, transparent 30%, var(--accent-deep) 60%, transparent 85%);
    opacity: 0.75;
  }
  .brand {
    position: absolute;
    top: 20px;
    left: 0;
    width: 100%;
    text-align: center;
    color: var(--white);
    font-family: "Montserrat", sans-serif;
    font-weight: 700;
  }
  .brand__mark {
    display: block;
    font-size: 34px;
    letter-spacing: 1px;
    line-height: 36px;
  }
  .brand__name {
    display: block;
    font-size: 9px;
    letter-spacing: 1.5px;
    line-height: 12px;
  }
  .product-name {
    position: absolute;
    top: 98px;
    left: 0;
    width: 100%;
    text-align: center;
    font-family: "Russo One", sans-serif;
    font-size: 40px;
    letter-spacing: 1px;
    color: var(--name);
    text-transform: uppercase;
  }
  .product-tag {
    position: absolute;
    top: 172px;
    left: 120px;
    font-family: "Russo One", sans-serif;
    text-transform: uppercase;
    line-height: 1;
  }
  .product-tag__new { display: block; font-size: 20px; color: var(--tag-new); }
  .product-tag__chew { display: block; font-size: 11px; color: var(--tag-chew); margin-left: 18px; letter-spacing: 1px; }

  .claim-band {
    position: absolute;
    top: 236px;
    left: 0;
    width: 100%;
    height: 56px;
    background: linear-gradient(90deg, var(--band-dark) 0%, var(--band-mid) 30%, var(--band-light) 50%, var(--band-mid) 70%, var(--band-dark) 100%);
    display: flex;
    align-items: center;
    justify-content: center;
    text-align: center;
    font-family: "Russo One", sans-serif;
    font-size: 18px;
    line-height: 22px;
    color: var(--band-text);
    text-shadow: 0 1px 2px rgba(0,0,0,0.6);
    text-transform: uppercase;
  }
  .label--red .claim-band { --band-light: #ffffff; --band-mid: #d4d4d4; --band-dark: #9c9c9c; }

  .benefits {
    position: absolute;
    top: 314px;
    left: 28px;
    width: 216px;
    margin: 0;
    padding: 0;
    list-style: none;
    color: var(--white);
    font-size: 10px;
    letter-spacing: 0.8px;
    line-height: 21px;
    white-space: nowrap;
    text-transform: uppercase;
  }
  .benefits li::before {
    content: "";
    display: inline-block;
    width: 6px;
    height: 6px;
    border-radius: 50%;
    background: var(--bullet);
    margin-right: 8px;
    vertical-align: 1px;
  }
  .label--red .benefits li::before { background: transparent; border: 1.5px solid var(--bullet); width: 4px; height: 4px; }

  .rule {
    position: absolute;
    top: 389px;
    left: 26px;
    width: 202px;
    height: 2px;
    background: linear-gradient(90deg, transparent, var(--rule) 15%, var(--rule) 85%, transparent);
  }
  .count {
    position: absolute;
    top: 397px;
    left: 0;
    width: 100%;
    text-align: center;
    color: var(--white);
    font-family: "Share Tech Mono", monospace;
    font-size: 13px;
    letter-spacing: 1px;
  }
</style>
</head>
<body>

  <section class="label label--blue">
    <div class="label__burst" role="img" aria-label="Blue light-streak burst artwork"></div>
    <div class="brand"><span class="brand__mark">KTV</span><span class="brand__name">KESTOVALE LABS</span></div>
    <div class="product-name">Catapult</div>
    <div class="product-tag"><span class="product-tag__new">New</span><span class="product-tag__chew">Chewable</span></div>
    <div class="claim-band">Bigger Stronger<br>Muscles</div>
    <ul class="benefits">
      <li>HMB, Vela ATP and KX-2</li>
      <li>All in one great tasting</li>
      <li>Workout supplement.</li>
    </ul>
    <div class="rule"></div>
    <div class="count">100 chewable tablet</div>
  </section>

  <section class="label label--orange">
    <div class="label__burst" role="img" aria-label="Orange light-streak burst artwork"></div>
    <div class="brand"><span class="brand__mark">KTV</span><span class="brand__name">KESTOVALE LABS</span></div>
    <div class="product-name">Catapult</div>
    <div class="product-tag"><span class="product-tag__new">New</span><span class="product-tag__chew">Chewable</span></div>
    <div class="claim-band">Bigger Stronger<br>Muscles</div>
    <ul class="benefits">
      <li>HMB, Vela ATP and KX-2</li>
      <li>All in one great tasting</li>
      <li>Workout supplement.</li>
    </ul>
    <div class="rule"></div>
    <div class="count">100 chewable tablet</div>
  </section>

  <section class="label label--red">
    <div class="label__burst" role="img" aria-label="Silver light-streak burst artwork"></div>
    <div class="brand"><span class="brand__mark">KTV</span><span class="brand__name">KESTOVALE LABS</span></div>
    <div class="product-name">Catapult</div>
    <div class="product-tag"><span class="product-tag__new">New</span><span class="product-tag__chew">Chewable</span></div>
    <div class="claim-band">Bigger Stronger<br>Muscles</div>
    <ul class="benefits">
      <li>HMB, Vela ATP and KX-2</li>
      <li>All in one great tasting</li>
      <li>Workout supplement.</li>
    </ul>
    <div class="rule"></div>
    <div class="count">100 chewable tablet</div>
  </section>

</body>
</html>
```